Corporate Business Card Design Project

..Hi designers!
I have established a consultancy within strategic communnications, for which I need a business card design - I've seen some of the things you do in here, and they're great! I'll provide some information in the following:
Name: BriarLedger
Tagline: Guiding Dialogue
Service: Strategic communications consulting (primariy internal communication and optimizing): various organisations - e.g. SMEs, NGOs and NPOs - are offered an analysis of their current efforts and, on the basis of that, management consulting tailored their unique challenges and needs.
It's a sole proprietorship - for now! - but it's my plan to employ 5-20 persons over the years. Therefore the card should NOT symbolize a start-up, but communicate a well-established, serious consultancy. Hence, it should also apply to serious companies and organizations - think Veltra or Hollis Brant Group (both as sender and receiver) ;)
The design should accordingly have a formal, conservative, stylish, corporate, clean look! and ditto colors, eg. black, grey, white etc - corresponding to the logo. The only colour that can appear is the same orange contrast as in my logo (see attachement). Not too bold or dramatic fonds or letters.
I choose the double sided as I think it gives the most professional look: One side with name, titel, phone, e-mail - then a little space - and four additional lines for address.
This composition is if all information should be in the same "column" - feel free to provide suggestions with the address places elsewhere on the one side.
On the other side, I'm only thinkin' something with the logo.
I'd be happy to see different ideas re. the use of the orange contrast, placement of logo, etc.
I do not plan on changing the design of businees cards ever - as I think it is more serious keeping a concept and avoid rebranding - and I'm sure that you can deliver an ever-lasting logo for my company! Thanks :).
Let's play the rest by ear in the correspondance.
Target Market(s)
Executive level: CEOs, HR directors, communication managers/directors, business owners.
Industry/Entity Type
Management Consulting

```html
<!DOCTYPE html>
<html lang="en">
<head>
<meta charset="utf-8">
<title>BriarLedger — Business Card</title>
<link rel="stylesheet" href="https://fonts.googleapis.com/css2?family=Fira+Sans:wght@300;400;500&display=swap">
<style>
  :root {
    --backdrop: #e4e4e2;
    --card-white: #ffffff;
    --card-black: #221f20;
    --ink: #1d1b1c;
    --accent: #e8761c;
    --muted: #8d8a88;
    --logo-white: #f2f1ef;
    --shadow: rgba(0, 0, 0, 0.18);
  }
  * { margin: 0; padding: 0; box-sizing: border-box; }
  html, body { width: 1200px; height: 873px; overflow: hidden; }
  body {
    background: var(--backdrop);
    font-family: "Fira Sans", Arial, sans-serif;
    color: var(--ink);
  }
  .canvas {
    position: relative;
    width: 1200px;
    height: 873px;
    display: flex;
    align-items: center;
    justify-content: center;
    gap: 60px;
  }
  .card {
    position: relative;
    width: 525px;
    height: 300px;
    box-shadow: 0 6px 22px var(--shadow);
    overflow: hidden;
  }

  /* Front: contact side */
  .card--front { background: var(--card-white); }
  .front__identity { position: absolute; left: 36px; top: 34px; }
  .front__name { font-size: 23px; font-weight: 400; letter-spacing: 0.2px; }
  .front__title { font-size: 17px; font-weight: 400; color: var(--accent); margin-top: 2px; }

  .front__contact {
    position: absolute; left: 200px; bottom: 98px;
    font-size: 17px; line-height: 1.35; font-weight: 400;
  }
  .front__address {
    position: absolute; right: 28px; bottom: 98px;
    font-size: 12.5px; line-height: 1.4; font-weight: 400;
  }
  .front__band {
    position: absolute; left: 0; right: 0; bottom: 0; height: 74px;
    background: var(--card-black);
    display: flex; align-items: center;
    padding-left: 36px;
  }
  .front__web {
    font-size: 16px; font-weight: 400; letter-spacing: 1.4px;
    color: var(--accent);
  }

  /* Back: logo side */
  .card--back { background: var(--card-black); }
  .wordmark {
    position: absolute; left: 50%; top: 50%;
    transform: translate(-50%, -58%);
    display: flex; flex-direction: column; align-items: flex-end;
  }
  .wordmark__row { display: flex; align-items: center; gap: 12px; }
  .wordmark__mark {
    width: 12px; height: 12px; background: var(--accent);
  }
  .wordmark__name {
    font-size: 42px; font-weight: 400; letter-spacing: 1.5px;
    color: var(--logo-white);
  }
  .wordmark__tagline {
    font-size: 11px; font-weight: 300; letter-spacing: 2.2px;
    color: var(--muted); margin-top: 4px;
  }
</style>
</head>
<body>
<main class="canvas">
  <section class="card card--front" aria-label="Business card, contact side">
    <div class="front__identity">
      <p class="front__name">Elias Warren</p>
      <p class="front__title">Position Title</p>
    </div>
    <div class="front__contact">
      <p>+44 (0) 207 94603185</p>
      <p>info@briarledger.com</p>
    </div>
    <address class="front__address" style="font-style: normal;">
      <p>12 Calder Row</p>
      <p>London, EC2A 4LT</p>
      <p>United Kingdom</p>
    </address>
    <div class="front__band">
      <p class="front__web">www.briarledger.com</p>
    </div>
  </section>

  <section class="card card--back" aria-label="Business card, logo side">
    <div class="wordmark">
      <div class="wordmark__row">
        <span class="wordmark__mark"></span>
        <span class="wordmark__name">BriarLedger</span>
      </div>
      <p class="wordmark__tagline">Guiding Dialogue</p>
    </div>
  </section>
</main>
</body>
</html>
```